Info Graphic about Maple Ridge Restaurant

This info graphic should detail all releavent details about Maple Ridge, such as opening hours, accepted payment methods, home delivery areas etc. please refer attached word document for details.

Also attached a pdf with old info graphic.

IMPORTANT:. Given there is lot of text, I expect the designer to make this interesting. This will be printed in A1 and also A4
Also, I need this in both Portrait and landscape designs.

Industry/Entity Type

Hospitality

Font styles to use
Serif
Sans Serif
Decorative
Script
Other font styles liked:
• I let designer choose

Colors

Designer to choose colors to be used in the design.

Requirements
Must have
• Refer attached word doc
Nice to have
• Refer attached word doc
Should not have
• Refer attached word doc

```html
<!DOCTYPE html>
<html lang="en">
<head>
<meta charset="utf-8">
<title>Maple Ridge Indian Restaurant – Info Sheet</title>
<link href="https://fonts.googleapis.com/css2?family=Open+Sans:ital,wght@0,400;0,600;0,700;1,600;1,700&family=Oswald:wght@600&display=swap" rel="stylesheet">
<style>
:root{
  --dark:#2a2a2a; --dark-2:#333334; --red:#e8323a; --orange:#f5a12d; --orange-text:#f58a24;
  --yellow:#f7c61a; --white:#ffffff; --light:#e7e7e9; --ink:#2b2b2b; --grey:#8d8d8d; --pill:#48484a;
}
*{margin:0;padding:0;box-sizing:border-box}
html,body{width:927px;height:1200px;overflow:hidden}
body{font-family:"Open Sans",sans-serif;background:var(--light);position:relative;color:var(--ink)}
.abs{position:absolute;line-height:1.15;white-space:nowrap}
.top-left{position:absolute;left:0;top:0;width:538px;height:682px;background:var(--dark)}
.top-right{position:absolute;left:538px;top:0;width:389px;height:682px;background:var(--dark-2)}
.order-band{position:absolute;left:0;top:682px;width:927px;height:81px;background:var(--red)}
.brand-mark{position:absolute;left:318px;top:34px;width:40px;height:40px;border-radius:50%;background:var(--red)}
.brand-name{left:381px;top:45px;font-size:27px;font-weight:700;color:var(--red)}
.brand-tag{left:381px;top:77px;font-size:15px;font-style:italic;font-weight:600;color:var(--red)}
.white{color:var(--white)}
.h-section{font-size:24px;font-weight:600}
.hours{position:absolute;left:72px;top:152px;width:422px;border-collapse:collapse;color:var(--white);font-size:14.5px}
.hours th{background:var(--red);text-align:left;font-size:18px;font-weight:600;height:21px;padding:0 0 0 13px;line-height:21px}
.hours td{height:25.9px;border-bottom:1px solid var(--red);padding:0 0 0 13px}
.hours tr:last-child td{border-bottom:none}
.hours .c1{width:105px}.hours .c2{width:171px}
.ph{position:absolute}
.pay-box{position:absolute;left:144px;top:437px;width:358px;font-size:13px;color:var(--ink)}
.pay-row{background:var(--orange);padding:0 10px;display:flex;align-items:center;line-height:1.1}
.pay-row.first{height:36px}
.pay-row.second{height:22px;border-top:1px solid var(--dark);white-space:nowrap}
.no-club{left:154px;top:504px;font-size:14.5px;font-style:italic;font-weight:700;color:var(--red)}
.voucher-title{left:144px;top:553px;font-size:24px;font-weight:600;color:var(--orange-text)}
.body-white{font-size:14.5px;color:var(--white)}
.mgr-pill{position:absolute;left:632px;top:158px;width:258px;height:71px;border-radius:12px;background:var(--pill)}
.reg-title{left:688px;top:273px;font-size:22px;font-weight:700;color:var(--yellow)}
.reg-line{font-size:11.5px;left:688px}
.red-title{font-size:22px;font-weight:600;color:var(--red)}
.book-phone{left:689px;top:632px;font-family:"Oswald",sans-serif;font-weight:600;font-size:25px;color:var(--yellow)}
.order-title{left:0;width:927px;text-align:center;top:688px;font-size:32px;font-weight:700;color:var(--orange-text);letter-spacing:1px}
.order-links{left:0;width:927px;text-align:center;top:728px;font-size:17px;font-weight:600;color:var(--white);word-spacing:2px}
.h-dark{font-size:22px;font-weight:600;color:var(--ink)}
.body-dark{font-size:14.5px;color:var(--ink)}
.byo-box{position:absolute;left:596px;top:840px;width:240px;height:80px;border-radius:6px;background:#d2d2d4}
ul.rules{list-style:none}
ul.rules li{position:relative;padding-left:11px}
ul.rules li::before{content:"•";position:absolute;left:0}
</style>
</head>
<body>
<div class="top-left"></div>
<div class="top-right"></div>

<!-- Brand -->
<div class="brand-mark"></div>
<div class="abs brand-name">Maple Ridge Indian Restaurant</div>
<div class="abs brand-tag">Your Best Indian Restaurant in Perth’s Northern Suburbs</div>

<!-- Opening hours -->
<div class="abs h-section white" style="left:85px;top:115px">Opening Hours</div>
<table class="hours">
  <tr><th class="c1">Day</th><th class="c2">Morning</th><th>Evening</th></tr>
  <tr><td>Monday</td><td>11:30AM-2:30PM</td><td>5:00PM – 9:00PM</td></tr>
  <tr><td>Tuesday</td><td>11:30AM-2:30PM</td><td>5:00PM – 9:00PM</td></tr>
  <tr><td>Wednesday</td><td>11:30AM-2:30PM</td><td>5:00PM – 9:00PM</td></tr>
  <tr><td>Thursday</td><td>11:30AM-2:30PM</td><td>5:00PM – 9:00PM</td></tr>
  <tr><td>Friday</td><td>11:30AM-2:30PM</td><td>5:00PM – 9:00PM</td></tr>
  <tr><td>Saturday</td><td>10:30AM-2:30PM</td><td>5:00PM – 9:00PM</td></tr>
  <tr><td>Sunday</td><td>10:30AM-2:30PM</td><td>5:00PM – 9:00PM</td></tr>
</table>

<!-- Payment -->
<div class="ph" role="img" aria-label="Wallet with banknotes illustration" style="left:52px;top:412px;width:88px;height:86px;border-radius:8px;background:linear-gradient(#8bc34a 0 12%,#6b6453 12%)"></div>
<div class="abs h-section white" style="left:154px;top:401px">Payment Methods</div>
<div class="pay-box">
  <div class="pay-row first">We accept cash, all Australian EFTPOS, Debit and Credit Cards.</div>
  <div class="pay-row second">We accept Charge cards – A surcharge of 2.8% apply.</div>
</div>
<div class="abs no-club">We DO NOT accept Club Cards</div>

<!-- Vouchers -->
<div class="ph" role="img" aria-label="Discount voucher ticket illustration" style="left:42px;top:564px;width:88px;height:60px;border-radius:6px;background:linear-gradient(160deg,#4a4a4a 0 40%,var(--orange) 40%)"></div>
<div class="abs voucher-title">Discount Vouchers</div>
<div class="abs body-white" style="left:144px;top:582px;line-height:20.8px">We accept City Saver Book Vouchers and<br>Maple Ridge supplied Discount vouchers.<br>City Saver Vouchers are eligible only for Dine-In.</div>

<!-- Management -->
<div class="mgr-pill"></div>
<div class="ph" role="img" aria-label="Portrait avatar of the restaurant manager" style="left:584px;top:140px;width:88px;height:88px;border-radius:50%;background:radial-gradient(circle at 50% 40%,#f2a23a 0 45%,var(--red) 46%);border:3px solid #555"></div>
<div class="abs white" style="left:688px;top:123px;font-size:22px;font-weight:600">New Management</div>
<div class="abs white" style="left:689px;top:161px;font-size:19px;font-weight:600">Rina Devaraj</div>
<div class="abs white" style="left:689px;top:184px;font-size:16px">0491570156</div>
<div class="abs white" style="left:689px;top:205px;font-size:16px">rina@mapleridge.com.au</div>

<!-- Registration -->
<div class="ph" role="img" aria-label="Map pin containing a hotel building illustration" style="left:568px;top:268px;width:104px;height:132px;border-radius:52px 52px 52px 52px / 52px 52px 80px 80px;background:radial-gradient(circle at 50% 38%,var(--yellow) 0 34%,#222 35% 40%,#5a5a5c 41%)"></div>
<div class="abs reg-title">Registration Details</div>
<div class="abs reg-line white" style="top:297px;font-weight:700">Cedar Lane Pty Ltd</div>
<div class="abs reg-line white" style="top:312px;font-weight:700">T/A Maple Ridge Restaurant</div>
<div class="abs reg-line white" style="top:328px">ABN: 12 345 678 901</div>
<div class="abs reg-line" style="top:344px;font-weight:700;color:var(--yellow)">Shop 4-5, 120 Harbour Street,</div>
<div class="abs reg-line" style="top:359px;font-weight:700;color:var(--yellow)">Woodvale, WA 6026, Australia</div>
<div class="abs reg-line" style="top:375px;color:var(--yellow)">Ph: 08 9000 1234</div>
<div class="abs reg-line" style="top:391px;color:var(--yellow)">Email: admin@mapleridge.com.au</div>

<!-- Buffet -->
<div class="ph" role="img" aria-label="Covered buffet dishes on a table illustration" style="left:574px;top:444px;width:94px;height:56px;border-radius:10px 10px 18px 18px;background:linear-gradient(#e8543a,#e8323a)"></div>
<div class="abs red-title" style="left:688px;top:428px">Dinner Buffet</div>
<div class="abs" style="left:689px;top:456px;font-size:14px;color:var(--red)">is available only from</div>
<div class="abs white" style="left:689px;top:473px;font-size:14px"><b style="font-size:18px;font-weight:600">Mon-Thu</b> from</div>
<div class="abs white" style="left:689px;top:497px;font-size:14px"><b style="font-weight:600">5:30</b>PM-<b style="font-weight:600">8:30</b>PM</div>

<!-- Booking -->
<div class="ph" role="img" aria-label="Dining table and chairs illustration" style="left:580px;top:558px;width:80px;height:80px;border-radius:50%;background:linear-gradient(160deg,#ee3a45,#c81e3c)"></div>
<div class="abs red-title" style="left:689px;top:536px">Book your Table</div>
<div class="abs white" style="left:691px;top:569px;font-size:14px">Please visit</div>
<div class="abs" style="left:691px;top:584px;font-size:15px;font-weight:700;font-style:italic;color:var(--red)">www.mapleridge.com.au</div>
<div class="abs white" style="left:691px;top:601px;font-size:14px">to book your table or</div>
<div class="abs white" style="left:691px;top:618px;font-size:14px">contact us on</div>
<div class="abs book-phone">08 9000 1234</div>

<!-- Order online -->
<div class="order-band"></div>
<div class="ph" role="img" aria-label="Online food ordering screen icon" style="left:50px;top:683px;width:76px;height:78px;border:3px solid var(--orange-text);border-radius:8px;opacity:.55"></div>
<div class="abs order-title">ORDER ONLINE</div>
<div class="abs order-links">www.mapleridge.com.au &nbsp;| &nbsp;www.quickplate.com.au &nbsp;| &nbsp;www.dinenow.com.au &nbsp;| &nbsp;www.fastfeast.com.au</div>

<!-- Delivery -->
<div class="abs h-dark" style="left:60px;top:790px">Home/Office Delivery</div>
<div class="abs body-dark" style="left:60px;top:818px;font-size:14px">We deliver to following suburbs</div>
<div class="abs body-dark" style="left:60px;top:849px;line-height:20.5px;font-size:14px">1.Beldon<br>2.Craigie<br>3.Darch<br>4.Duncraig</div>
<div class="abs body-dark" style="left:142px;top:849px;line-height:20.5px;font-size:14px">5.Edgewater<br>6.Greenwood<br>7.Hocking<br>8.Kingsley</div>
<div class="abs body-dark" style="left:247px;top:849px;line-height:20.5px;font-size:14px">9.Madeley<br>10.Padbury<br>11.Pearsall<br>12.Wangara</div>
<div class="abs body-dark" style="left:340px;top:849px;font-size:14px">13.Woodvale</div>
<div class="abs" style="left:54px;top:940px;font-size:15px;font-weight:600">Delivery Charges $5 and minimum order value $30</div>

<!-- BYO -->
<div class="byo-box"></div>
<div class="ph" role="img" aria-label="Wine bottles in an ice bucket illustration" style="left:506px;top:804px;width:96px;height:116px;background:linear-gradient(#5a5a5a 0 55%,#a9a9ab 55%);border-radius:4px"></div>
<div class="abs" style="left:622px;top:846px;font-size:20px;font-weight:600">BYO</div>
<div class="abs" style="left:622px;top:871px;font-size:14.5px;font-weight:600">BYO allowed – only for Wine.</div>
<div class="abs" style="left:622px;top:892px;font-size:14.5px;font-weight:600;font-style:italic">Charges per bottle apply</div>

<!-- House rules -->
<div class="ph" role="img" aria-label="Pointing hand and checklist icon" style="left:52px;top:996px;width:132px;height:44px;background:#c9c9cb;border-radius:3px"></div>
<svg class="ph" style="left:106px;top:1002px" width="70" height="30" viewBox="0 0 70 30"><path d="M4 14l6 6 12-12" stroke="#444" stroke-width="3" fill="none"/><path d="M44 8l10 10M54 8L44 18" stroke="#444" stroke-width="3"/><path d="M0 26h28M38 26h28" stroke="#444" stroke-width="2"/></svg>
<div class="abs h-dark" style="left:55px;top:1040px">House Rules</div>
<ul class="abs rules body-dark" style="left:55px;top:1069px;line-height:20.2px">
  <li>Prices are inclusive of GST</li>
  <li>Prices are subject to change without notice</li>
  <li>Outside Food and Beverages (except WINE)<br>are not allowed</li>
</ul>

<!-- Facilities -->
<div class="ph" role="img" aria-label="Baby high chair icon" style="left:478px;top:1004px;width:34px;height:80px;background:#5d5d5f;border-radius:3px;opacity:.85"></div>
<div class="ph" role="img" aria-label="Wheelchair access icon" style="left:514px;top:984px;width:56px;height:56px;background:#8d8d8f;border-radius:3px"></div>
<div class="abs h-dark" style="left:513px;top:1040px">Facilities</div>
<div class="abs body-dark" style="left:513px;top:1069px;line-height:20.2px;font-size:14px">Wheel chair access<br>Disabled Toilet inside<br>Baby Changer table<br>High rise tables for babies<br>Music System</div>

<!-- Warning -->
<svg class="ph" style="left:724px;top:960px" width="76" height="68" viewBox="0 0 76 68"><path d="M38 3 Q42 3 44 7 L73 58 Q75 65 68 65 L8 65 Q1 65 3 58 L32 7 Q34 3 38 3Z" fill="var(--red)"/><rect x="34" y="18" width="8" height="28" rx="4" fill="#fff"/><circle cx="38" cy="55" r="5" fill="#fff"/></svg>
<div class="abs h-dark" style="left:725px;top:1041px;font-size:23px">Warning</div>
<div class="abs body-dark" style="left:725px;top:1069px;line-height:20.2px;font-size:14px">Please inform wait<br>staff for any allergies.<br>Food consumed at<br>your own risk.</div>
</body>
</html>
```